Roofing company in Toronto, Canada needs a logo design and business card design

We need a business card and logo created for our company. Our company is "KVL Roofing" which provides roofing services for commercial and residential customers. We serve customers in the Greater Toronto Area (in Canada) thus the name KVL.

We want the logo and business card to be a modern design displaying professionalism and quality in the work. We would prefer rounded corners for the business cards but are open to other ideas. The cards should be pleasant and appealing to customers.

Target Market(s)

Commercial and Residential customers

Industry/Entity Type

Roofing

Contact Information for Business Card

Logo Text

KVL Roofing

Requirements
Nice to have
• Colours that are pleasing to the eye but at the same time should stand out from other business cards. If the design can incorporate the name of KVL Roofing and the actual concept of roofing that would be nice.
Should not have
• Do not want the business cards or logo to be childish looking. Need to look professionally designed.

```html
<!DOCTYPE html>
<html lang="en">
<head>
<meta charset="utf-8">
<title>KVL Roofing – Business Card</title>
<link href="https://fonts.googleapis.com/css2?family=Lato:wght@400;700;900&display=swap" rel="stylesheet">
<style>
  :root {
    --stage: #3b3532;
    --card-black: #0b0b0b;
    --card-white: #ffffff;
    --ink: #111111;
    --red: #e32227;
    --paper-text: #1a1a1a;
  }
  * { box-sizing: border-box; margin: 0; padding: 0; }
  html, body { width: 1200px; height: 780px; overflow: hidden; }
  body {
    background: var(--stage);
    font-family: "Lato", Arial, sans-serif;
    position: relative;
  }
  .card {
    position: absolute;
    top: 240px;
    width: 520px;
    height: 300px;
    border-radius: 14px;
    overflow: hidden;
    box-shadow: 0 14px 30px rgba(0,0,0,0.45);
  }
  .card--front { left: 50px; background: var(--card-black); }
  .card--back  { left: 630px; background: var(--card-white); }

  .brand {
    display: flex;
    align-items: center;
    gap: 12px;
    font-weight: 900;
    letter-spacing: 1px;
  }
  .brand__mark {
    width: 30px; height: 30px;
    background: var(--red);
  }
  .card--front .brand {
    position: absolute;
    left: 50%; top: 50%;
    transform: translate(-50%, -50%);
    font-size: 46px;
    color: #ffffff;
  }
  .card--back .brand {
    position: absolute;
    left: 34px; top: 34px;
    font-size: 34px;
    color: var(--ink);
  }
  .card--back .brand__mark { width: 24px; height: 24px; }

  .person {
    position: absolute;
    left: 34px; top: 104px;
  }
  .person__name {
    font-weight: 900;
    font-size: 19px;
    color: var(--paper-text);
    letter-spacing: 0.5px;
  }
  .person__title {
    font-size: 14px;
    color: var(--red);
    margin-top: 2px;
  }
  .contact {
    position: absolute;
    left: 34px; top: 170px;
    list-style: none;
  }
  .contact__item {
    display: flex;
    align-items: center;
    gap: 9px;
    font-size: 14px;
    color: var(--paper-text);
    height: 22px;
  }
  .contact__icon {
    width: 16px; height: 16px;
    border-radius: 3px;
    background: var(--red);
    display: flex; align-items: center; justify-content: center;
  }
  .contact__icon svg { width: 11px; height: 11px; }

  .accent-area {
    position: absolute;
    right: 0; bottom: 0;
    width: 200px; height: 190px;
    background: var(--red);
    border-top-left-radius: 30px;
  }
</style>
</head>
<body>

  <section class="card card--front">
    <div class="brand"><span class="brand__mark"></span>KVL Roofing</div>
  </section>

  <section class="card card--back">
    <div class="brand"><span class="brand__mark"></span>KVL Roofing</div>

    <div class="person">
      <p class="person__name">MARCUS HALE</p>
      <p class="person__title">Managing Director</p>
    </div>

    <ul class="contact">
      <li class="contact__item">
        <span class="contact__icon"><svg viewBox="0 0 12 12"><path d="M2 1h3l1 3-1.5 1a6 6 0 0 0 2.5 2.5L8 6l3 1v3c-5 1-10-4-9-9z" fill="#fff"/></svg></span>
        (416) 555 0142
      </li>
      <li class="contact__item">
        <span class="contact__icon"><svg viewBox="0 0 12 12"><rect x="3" y="1" width="6" height="10" rx="1" fill="#fff"/></svg></span>
        (416) 555 0142
      </li>
      <li class="contact__item">
        <span class="contact__icon"><svg viewBox="0 0 12 12"><rect x="1" y="3" width="10" height="7" fill="#fff"/><path d="M1 3l5 4 5-4" stroke="#e32227" fill="none"/></svg></span>
        info@kvlroofing.ca
      </li>
      <li class="contact__item">
        <span class="contact__icon"><svg viewBox="0 0 12 12"><circle cx="6" cy="6" r="4.5" stroke="#fff" fill="none"/><path d="M1.5 6h9M6 1.5v9" stroke="#fff"/></svg></span>
        www.kvlroofing.ca
      </li>
    </ul>

    <div class="accent-area" role="img" aria-label="Large red maple leaf decoration"></div>
  </section>

</body>
</html>
```